Medical Call Centre Needs a Web Design

We need a web design for a new company based in Melbourne called "Vantorra Services". We provide medical centres with administrative support by managing inbound calls to our clients facility. We require a clean, simple and easy to navigate website with an ultimate end product alike this - http://www.pelmarko.com/

The final design should communicate professionalism, new age and inovative.

Industry/Entity Type

It Company

```html
<!DOCTYPE html>
<html lang="en">
<head>
<meta charset="utf-8">
<title>Vantorra Services</title>
<link href="https://fonts.googleapis.com/css2?family=Arimo:wght@400;700&display=swap" rel="stylesheet">
<style>
:root{
  --yellow:#f3c43f;
  --yellow-deep:#e9b52c;
  --dark:#262626;
  --darker:#1b1b1b;
  --ink:#1f1f1f;
  --white:#ffffff;
  --light:#efefef;
  --pill:#e9e9e9;
}
*{margin:0;padding:0;box-sizing:border-box}
html,body{width:1200px;height:2682px;overflow:hidden}
body{font-family:"Arimo",Arial,sans-serif;color:var(--ink);background:var(--white);position:relative}
section,header,footer{position:absolute;left:0;width:1200px}
.abs{position:absolute}

/* header */
.site-header{top:0;height:150px;background:var(--yellow)}
.brand{left:150px;top:40px;color:var(--white);font-weight:700;font-size:30px;line-height:30px}
.phone{right:40px;top:4px;font-size:13px;color:var(--white)}
.main-nav{left:436px;top:0;display:flex;height:107px}
.main-nav a{display:flex;align-items:center;padding:0 22px;font-size:13px;color:var(--white);text-decoration:none;border-right:1px solid rgba(255,255,255,.5)}
.main-nav a.active{background:var(--dark);padding:0 28px;border:none}

/* hero */
.hero{top:150px;height:470px;background:linear-gradient(100deg,#c8d6e4 0%,#eef2f6 40%,#f2dccd 60%,#f4f4f4 100%)}
.hero-caption{left:150px;top:208px;width:420px}
.hero-title{background:var(--yellow);color:var(--white);font-weight:700;font-size:36px;padding:8px 12px;height:62px}
.hero-text{background:rgba(30,30,30,.88);color:var(--white);font-size:17px;line-height:20px;padding:12px 12px 18px}
.hero-arrows{left:523px;top:425px;display:flex;gap:4px}
.hero-arrows span{width:46px;height:50px;background:var(--yellow);display:flex;align-items:center;justify-content:center}

/* about */
.about{top:620px;height:258px;background:var(--dark);color:var(--white)}
.about h2{left:190px;top:70px;font-weight:400;font-size:48px;color:var(--yellow)}
.about p{left:190px;top:140px;width:840px;font-size:15px;line-height:20px}

h2.section-title{position:absolute;left:178px;font-weight:400;font-size:50px;line-height:56px;color:var(--ink)}
.body-text{font-size:16px;line-height:22px}
.small-text{font-size:14px;line-height:18px}

/* goals */
.goals{top:878px;height:329px;background:var(--white)}
.goals h2{top:45px}
.goals ol{left:180px;top:130px;font-size:16px;line-height:30px;list-style:none}
.goals-photo{left:754px;top:44px;width:251px;height:285px;background:linear-gradient(180deg,#e4e7ea,#c9b7a6)}

/* overview */
.overview{top:1207px;height:469px;background:var(--yellow)}
.overview h2{top:40px}
.overview .body-text{left:190px;width:830px}
.tabs{left:218px;top:273px;width:762px;height:96px;background:var(--pill);border-radius:22px}
.tab-label{top:36px;font-size:19px;color:var(--ink)}
.tab-circle{left:301px;top:-36px;width:168px;height:168px;border-radius:50%;background:var(--darker);border:4px solid var(--white);color:var(--white);display:flex;align-items:center;justify-content:center;font-size:19px}

/* benefits */
.benefits{top:1676px;height:335px;background:var(--white)}
.benefits h2{top:12px}
.benefits .small-text{left:190px}
.benefits ul{left:190px;top:128px;font-size:14px;line-height:20px;list-style:none}
.benefits ul li::before,.contact ul li::before{content:"• "}
.dashboard{left:778px;top:146px;width:228px;height:156px;background:linear-gradient(180deg,#f4f6f8,#dfe8ef)}

/* contact */
.contact{top:2011px;height:470px;background:var(--light)}
.contact h2{top:32px}
.contact .small-text{left:190px}
.contact ul{left:190px;top:248px;font-size:14px;line-height:20px;list-style:none}
.contact-photo{left:855px;top:262px;width:168px;height:208px;background:linear-gradient(180deg,#e9e4df,#c9aa92)}

/* footer */
.site-footer{top:2481px;height:201px;background:var(--dark);color:var(--white)}
.footer-nav{left:300px;top:0;display:flex;height:60px}
.footer-nav a{display:flex;align-items:center;padding:0 22px;font-size:13px;color:var(--white);text-decoration:none;border-right:1px solid rgba(255,255,255,.3)}
.footer-nav a.active{background:var(--darker);padding:0 26px}
.follow{left:0;width:1200px;top:84px;text-align:center;font-size:13px}
.social{left:578px;top:108px;display:flex;gap:8px}
.social span{width:18px;height:18px;background:#3a6db3;border-radius:2px}
.social span+span{background:#3aa2dc}
</style>
</head>
<body>

<header class="site-header">
  <div class="abs brand">vantorra<br>services</div>
  <div class="abs phone">Phone: 555-014-2290</div>
  <nav class="abs main-nav">
    <a class="active" href="#">HOME</a><a href="#">ABOUT US</a><a href="#">OUR GOAL</a><a href="#">OVERVIEW</a><a href="#">BENEFITS</a><a href="#">CONTACT US</a>
  </nav>
</header>

<section class="hero" role="img" aria-label="Smiling call centre agent wearing a headset">
  <div class="abs hero-caption">
    <div class="hero-title">LOREM IPSUM DOLOR</div>
    <div class="hero-text">Lorem ipsum dolor sit amet, consectetur adipiscing elit, sed do eiusmod tempor incididunt ut labore et dolore magna aliqua. Ut enim ad minim veniam, quis nostrud exercitation ullamco laboris nisi ut aliquip ex ea commodo consequat.</div>
  </div>
  <div class="abs hero-arrows">
    <span><svg width="14" height="18" viewBox="0 0 14 18"><path d="M11 2 3 9l8 7" fill="none" stroke="#fff" stroke-width="2.5"/></svg></span>
    <span><svg width="14" height="18" viewBox="0 0 14 18"><path d="m3 2 8 7-8 7" fill="none" stroke="#fff" stroke-width="2.5"/></svg></span>
  </div>
</section>

<section class="about">
  <h2 class="abs">About Us</h2>
  <p class="abs">Vantorra Services is an Australian owned company who will provide a support network to your administration team (working together) by removing some of the daily distractions and managing your inbound calls. Acting as a switchboard for your organisation and providing exceptional customer service.</p>
</section>

<section class="goals">
  <h2 class="section-title">OUR GOALS</h2>
  <ol class="abs">
    <li>1. Simple and easy to do business with</li>
    <li>2. Proactive and transparent with information, news and changes</li>
    <li>3. Best-in-class and independently assessed</li>
    <li>4. Delivering a premium patient experience</li>
  </ol>
  <div class="abs goals-photo" role="img" aria-label="Two smiling business professionals"></div>
</section>

<section class="overview">
  <h2 class="section-title">OVERVIEW</h2>
  <p class="abs body-text" style="top:125px">Vantorra Services aim to change the way medical facilities interact with patients, by assisting with the management of inbound calls - an industry initiative to encourage and support the growth of patient care and customer service.</p>
  <p class="abs body-text" style="top:192px">The medical industry over recent years has seen a growth in terms of service quality, efficiency, and availability. In addition, medical standards are continually evolving to embrace the use of IT within the medical industry.</p>
  <div class="abs tabs">
    <span class="abs tab-label" style="left:75px">CULTURE</span>
    <div class="abs tab-circle">ORGANIZATION</div>
    <span class="abs tab-label" style="left:500px">CHANGE / INITIATIVE</span>
  </div>
</section>

<section class="benefits">
  <h2 class="section-title">BENEFITS</h2>
  <p class="abs small-text" style="top:82px;width:560px">Vantorra Services will allow you to explore unmeasured communication activities currently unmonitored by your facility. Have you ever considered the following</p>
  <ul class="abs">
    <li>Volume</li><li>Talk time</li><li>Queue time</li><li>Abandoned calls</li><li>Quality assurance</li>
  </ul>
  <p class="abs small-text" style="top:236px;width:540px">By utilising our service, we will enable your facility to enhance the image and identify needs and resources required to offer the best possible service within the medical industry. Cultivate and conduct evidence based decision making and take time to understand your callers.</p>
  <div class="abs dashboard" role="img" aria-label="Call statistics dashboard with gauges and a line chart"></div>
</section>

<section class="contact">
  <h2 class="section-title">CONTACT US</h2>
  <p class="abs small-text" style="top:105px;width:620px">Vantorra Services will manage a diverted telecommunications environment through the professional management of inbound calls to your facility. Having developed tailored protocols and message scripts, we will provide a consistent level of service, giving callers the time they deserve without interruption.</p>
  <p class="abs small-text" style="top:190px;width:620px">Providing exceptional supportive services with a primary focus in the following categories:</p>
  <ul class="abs">
    <li>General Enquiries</li><li>Account Enquiries</li><li>Appointments</li><li>Results</li><li>Internal</li>
  </ul>
  <div class="abs contact-photo" role="img" aria-label="Smiling receptionist wearing a headset"></div>
</section>

<footer class="site-footer">
  <nav class="abs footer-nav">
    <a class="active" href="#">HOME</a><a href="#">ABOUT US</a><a href="#">OUR GOAL</a><a href="#">OVERVIEW</a><a href="#">BENEFITS</a><a href="#">CONTACT US</a>
  </nav>
  <div class="abs follow">FOLLOW US</div>
  <div class="abs social"><span></span><span></span></div>
</footer>

</body>
</html>
```